PowerPoint Re-Design and Template Needs a Designer's Eye!

I have the text, images and logo for a PowerPoint but need your Design and Template skills! Less than 20 pages, needs to be concise, include images, must have creative page layouts, include our floater-logo on every page, use sidebars or call-outs for important information, have color but not too much because this will be printed many times (our current colors are too dark). You can use bullet-points or paragraphs. You can also change the titles, font, color, layout - anything! This is YOUR PowerPoint to create the most impressive Template! We are an investment management firm located in New York City. Our investment returns are the very best in the industry and we want this PowerPoint to convey our "best in class" style.

Notes:
1) Please use the PPP outline attached.
2) I have attached a rough draft PPP. Please use the logos on page 2. Some pages do not have text, the final text will be available shortly.
3) I have attached examples you can reference.
4) Please include our floater-logo on every page.
5) Please feel free to ask questions or clarification.
Updates

Hi Designers, Thank you very much for your wonderful submissions! My partners and I are going through each submission in detail today and tomorrow. We'll be in touch over the next few days with additional questions and comments. Stay tuned! Best, Marcus Vandell

Target Market(s)

High-net worth individuals and institutions. New York City, Wall Street.

Industry/Entity Type

Investment

Requirements
Must have
• - Floater-logo on every page
- Sidebars or call-outs on several pages (you can decide which ones)
- Please include images; however, the PPP Template is the most important.

```html
<!DOCTYPE html>
<html lang="en">
<head>
<meta charset="utf-8">
<title>Summit Crest Asset Management – Slide Template</title>
<link rel="stylesheet" href="https://fonts.googleapis.com/css2?family=Open+Sans:wght@400;600&family=Questrial&display=swap">
<style>
:root{
  --board:#5f5f61;
  --orange:#f28c28;
  --orange-deep:#e07a1c;
  --peach:#fbc59a;
  --peach-light:#fde3cc;
  --ink:#2b2b2b;
  --grey:#8a8a8a;
  --white:#ffffff;
}
*{margin:0;padding:0;box-sizing:border-box}
html,body{width:1200px;height:848px;overflow:hidden;background:var(--board)}
body{position:relative;font-family:"Open Sans",Arial,sans-serif;color:var(--ink)}
.slide{position:absolute;overflow:hidden;background:var(--white)}
.slide--cover{left:48px;top:22px;width:528px;height:396px}
.slide--title{left:624px;top:30px;width:526px;height:394px;
  background:linear-gradient(180deg,#f9c394 0%,#fde6d2 45%,#fff7f0 60%,#fbd2ae 100%)}
.slide--disclaimer{left:53px;top:433px;width:522px;height:392px}
.slide--contents{left:627px;top:433px;width:520px;height:390px}

.brand{position:absolute;text-align:center}
.brand__name{display:flex;align-items:center;justify-content:center;gap:6px;
  font-family:"Questrial",sans-serif;color:var(--orange);font-size:24px;letter-spacing:.5px;
  border-bottom:1px solid var(--peach);padding-bottom:2px}
.brand__dot{width:20px;height:20px;border-radius:50%;background:var(--orange)}
.brand__sub{font-family:"Questrial",sans-serif;color:var(--grey);font-size:9.5px;letter-spacing:2.6px;margin-top:3px}
.slide--cover .brand{left:150px;top:165px;width:230px}
.slide--title .brand{left:278px;top:192px;width:200px}
.slide--title .brand__name{font-size:21px}
.slide--title .brand__dot{width:18px;height:18px}

.emblem{position:absolute;border-radius:50%;background:var(--orange)}
.slide--title .emblem{left:-150px;top:28px;width:400px;height:340px;border-radius:50%}

.footer{position:absolute;bottom:4px;left:0;width:100%;text-align:center;font-size:7.5px;color:var(--grey)}

.hero{position:absolute;left:0;top:0;width:100%;height:157px;
  background:linear-gradient(180deg,#c9733a 0%,#e4925a 55%,#efa878 100%)}
.hero__title{position:absolute;right:28px;top:44px;font-family:"Questrial",sans-serif;font-size:21px;color:var(--white);letter-spacing:.5px}
.disclaimer-text{position:absolute;left:28px;top:164px;width:470px;font-size:7.4px;line-height:10.4px;color:#333}
.disclaimer-text p{margin-bottom:10px}
.floater{position:absolute;right:14px;bottom:8px;width:28px;height:28px;border-radius:50%;background:var(--orange)}

.tab{position:absolute;right:47px;top:0;width:23px;height:32px;background:#111;color:var(--white);
  font-size:7px;text-align:center;padding-top:9px;clip-path:polygon(0 0,100% 0,100% 75%,50% 100%,0 75%)}
.contents-title{position:absolute;left:28px;top:29px;font-family:"Questrial",sans-serif;font-size:19px;color:var(--ink)}
.contents-title strong{color:var(--orange);font-weight:600;font-family:"Open Sans",sans-serif}
.ring{position:absolute;left:26px;top:102px;width:200px;height:200px;border-radius:50%;border:1px solid #777}
.ring .emblem{left:12px;top:12px;width:174px;height:174px}
.toc{list-style:none}
.toc__item{position:absolute;height:22px;background:var(--peach);border-radius:11px;
  display:flex;align-items:center;font-size:11px;color:var(--ink)}
.toc__num{width:25px;height:25px;border-radius:50%;background:var(--peach-light);border:1.5px solid var(--orange-deep);
  display:flex;align-items:center;justify-content:center;font-size:11px;margin-left:-2px;margin-right:9px}
</style>
</head>
<body>

<section class="slide slide--cover">
  <div class="brand">
    <div class="brand__name"><span>SUMMIT</span><span class="brand__dot"></span><span>CREST</span></div>
    <div class="brand__sub">ASSET MANAGEMENT, LLC</div>
  </div>
</section>

<section class="slide slide--title">
  <div class="emblem" aria-hidden="true"></div>
  <div class="brand">
    <div class="brand__name"><span>SUMMIT</span><span class="brand__dot"></span><span>CREST</span></div>
    <div class="brand__sub">ASSET MANAGEMENT, LLC</div>
  </div>
  <div class="footer">Marcus Vandell 2015</div>
</section>

<section class="slide slide--disclaimer">
  <div class="hero" role="img" aria-label="Photograph of three classical stone column bases in warm orange light"></div>
  <h2 class="hero__title">DISCLAIMER</h2>
  <div class="disclaimer-text">
    <p>This presentation and its contents are a confidential communication. The information contained here in is proprietary and belongs solely to SUMMIT CREST Asset Management, LLC. SUMMIT CREST Asset Management, LLC (hereinafter referred to as the “Management Company”) is a limited liability company incorporated in the state of New York and governed by the laws of New York. No reproduction or distribution of this information, in whole or in part, is permissible without prior written consent of the Management Company.</p>
    <p>This presentation has been prepared solely for informational purposes and does not offer investment advice. This presentation does not recommend the purchase or sale of a limited partnership interest, share, securities or units. If any offer to purchase a limited partnership interest, share, securities of units into the Management Company is made, it shall be pursuant to a definitive private placement Memorandum prepared by, or on behalf of the Management Company and shall supersede the information contained herein its entirety. Any decision to invest should be made only after said investor has consulted with appropriate licensed investment, tax accounting and legal advisors and the advisors collectively deem an investment is suitable for said investor</p>
    <p>It is possible that an investment lose money. Investing is speculative in nature and performance results can be volatile. Past performance is not indicative of future performance. Many factors affect investment results; including but not limited to changes in the market economy, political environment or financial developments.</p>
    <p>Under no circumstances does the content of this presentation represent a recommendation to buy or sell a limited partnership interest, shares, securities or units</p>
  </div>
  <div class="floater" aria-hidden="true"></div>
  <div class="footer">Marcus Vandell 2015</div>
</section>

<section class="slide slide--contents">
  <div class="tab">02</div>
  <h2 class="contents-title">TABLES OF <strong>CONTENTS</strong></h2>
  <div class="ring"><div class="emblem" aria-hidden="true"></div></div>
  <ol class="toc">
    <li class="toc__item" style="left:212px;top:98px;width:227px"><span class="toc__num">1</span>Investment Highlights</li>
    <li class="toc__item" style="left:234px;top:138px;width:225px"><span class="toc__num">2</span>Investment Strategy Overview</li>
    <li class="toc__item" style="left:252px;top:190px;width:226px"><span class="toc__num">3</span>Investment Strategy Process</li>
    <li class="toc__item" style="left:238px;top:238px;width:227px"><span class="toc__num">4</span>Investment Strategy Analysis</li>
    <li class="toc__item" style="left:212px;top:284px;width:227px"><span class="toc__num">5</span>Service Providers</li>
  </ol>
  <div class="footer">Marcus Vandell 2015</div>
</section>

</body>
</html>
```